Grand Opening for Brightvale Church

Would like to have a BillBoard Created according to the specs listed by the company who will be producing the print. I am attaching the spec sheet to this post. I am also attaching a couple different picture options as well as a former Billboard design that was done. I would like the design to incorporate my logo, picture. I am okay if the background on the picture is eliminated for creative purposes. The words to be displayed is "Grand Opening" April 12, 2020 at the former Halden Middle School) 71st Marsh Hollow Rd.

Colors

Designer to choose colors to be used in the design.

Requirements
Must have
• Something that pops
Nice to have
• Good color coordinations and clearly visible text

```html
<!DOCTYPE html>
<html lang="en">
<head>
<meta charset="utf-8">
<title>Brightvale Church – Grand Opening Billboard</title>
<link rel="stylesheet" href="https://fonts.googleapis.com/css2?family=Montserrat:wght@300;400;600;800&display=swap">
<style>
  :root {
    --stage: #5e5e5e;
    --board: #f4f4f4;
    --ink: #2f2f2f;
    --orange: #f39233;
    --black: #0d0d0d;
    --rust: #b5642a;
    --denim: #8a8f96;
  }
  * { margin: 0; padding: 0; box-sizing: border-box; }
  html, body {
    width: 1002px; height: 1200px; overflow: hidden;
    background: var(--stage);
    font-family: "Montserrat", Arial, sans-serif;
  }
  .billboard {
    position: absolute; left: 31px; top: 383px;
    width: 940px; height: 433px;
    background: radial-gradient(circle at 72% 40%, #ffffff 0%, var(--board) 60%, #ececec 100%);
    overflow: hidden;
    box-shadow: 0 4px 10px rgba(0,0,0,.35);
  }
  .church-name {
    position: absolute; left: 128px; top: 40px;
    color: var(--ink); font-weight: 600;
    font-size: 62px; line-height: 1.05; letter-spacing: -0.5px;
  }
  .church-name .mark {
    display: inline-block; width: 22px; height: 22px;
    border-radius: 50%; background: var(--orange);
    margin-right: 12px; vertical-align: middle;
  }
  .banner { position: absolute; left: 46px; top: 226px; width: 526px; height: 84px; }
  .headline {
    position: absolute; left: 46px; top: 232px; width: 526px;
    text-align: center; color: var(--orange);
    font-weight: 800; font-size: 50px; letter-spacing: 1px; line-height: 66px;
  }
  .date {
    position: absolute; left: 0; top: 314px; width: 620px;
    text-align: center; color: var(--orange); font-size: 52px; line-height: 56px;
  }
  .date strong { font-weight: 800; }
  .date span { font-weight: 300; }
  .venue {
    position: absolute; left: 0; top: 384px; width: 620px;
    text-align: center; font-size: 17px; line-height: 22px;
  }
  .venue .school { color: var(--orange); font-weight: 800; letter-spacing: .3px; }
  .venue .divider { color: var(--ink); margin: 0 6px; font-weight: 300; }
  .venue .street { color: var(--ink); font-weight: 600; }
  .speaker-photo {
    position: absolute; left: 560px; top: 28px; width: 296px; height: 405px;
    background: linear-gradient(180deg, #d9b79b 0%, var(--rust) 35%, #9c5422 75%, var(--denim) 100%);
    border-radius: 120px 120px 0 0;
    opacity: .9;
  }
</style>
</head>
<body>
  <main class="billboard">
    <div class="church-name"><span class="mark"></span>Brightvale<br>Church</div>

    <svg class="banner" viewBox="0 0 526 84" aria-hidden="true">
      <polygon points="0,3 30,3 14,30" fill="var(--orange)"/>
      <polygon points="508,24 526,22 518,48" fill="var(--orange)"/>
      <polygon points="46,84 508,76 500,84" fill="var(--orange)"/>
      <polygon points="28,0 500,22 512,76 0,84" fill="var(--black)"/>
    </svg>
    <div class="headline">GRAND OPENING</div>

    <div class="date"><strong>APRIL 12</strong>, <span>2020</span></div>

    <div class="venue">
      <span class="school">HALDEN MIDDLE SCHOOL</span><span class="divider">|</span><span class="street">71st Marsh Hollow Rd</span>
    </div>

    <div class="speaker-photo" role="img" aria-label="Photo of the pastor speaking with open hands, wearing a rust corduroy blazer, striped shirt and jeans"></div>
  </main>
</body>
</html>
```